Grins of Pellbrook - Dental, needs a redesign

Purpose:
Redesign website: http://www.grinsofpellbrook.example/

Sections are important, but for content, we can use existing website or have some placeholder text to fill in later.

Some of the required sections:
About us, contact us, services, our offices, our staff, patient education, patient forms (link to Molavex can be used here), link to friendspace, testimonials

Editability:
We would like to be able to update and edit the content in the future, for small changes

Pictures:
Here is a link to the staff pictures we’d like to use on the website:
https://www.filecrate.example/sh/493kq7zz2tt118p5/BBDRmwLe_uKPi8ZrafQWTGeeb?dl=0
You don't have to use all the pictures; just a few.

friendspace page:
https://www.friendspace.example/Grins-of-Pellbrook-627150384019562

Colors: Calming colors/images for a soothing feeling... to assure the patient that it'll not be that bad.

Target Market(s)

General population

Industry/Entity Type

Dental Clinic

Coding

Coded - Design and coding required

Number of Pages Required

5+ page

Requirements
Must have
• About us, contact us, services, our offices, our staff, patient education, patient forms (link to Molavex can be used here), link to friendspace, testimonials.
• Just create the placeholders for content or use from existing website.
• The staff picture of everyone needs to be on the home page - because that makes it more personal and has received positive feedback from many patients.

```html
<!DOCTYPE html>
<html lang="en">
<head>
<meta charset="utf-8">
<title>Grins of Pellbrook - Dental</title>
<link rel="stylesheet" href="https://fonts.googleapis.com/css2?family=Poppins:wght@300;400;500;700&display=swap">
<style>
:root{
  --header-bg:#e6e6e6;
  --band-light:#f4f4f4;
  --band-mid:#ededed;
  --ink:#1f2a36;
  --accent:#3aaccc;
  --btn-1:#3aaccc;
  --btn-2:#00c2ef;
  --btn-3:#7fe0f8;
  --curve:#8fdcef;
  --footer-bg:#e6e6e6;
}
*{margin:0;padding:0;box-sizing:border-box}
html,body{width:1200px;height:1200px;overflow:hidden;background:#fff}
body{position:relative;font-family:'Poppins',sans-serif;color:var(--ink)}
.abs{position:absolute}

.site-header{left:0;top:0;width:1200px;height:100px;background:var(--header-bg)}
.brand-mark{left:216px;top:30px;width:34px;height:34px;border-radius:50%;background:var(--accent)}
.brand-name{left:270px;top:22px;font-size:17px;font-weight:500;white-space:nowrap}
.brand-tagline{left:308px;top:50px;font-size:14px;font-weight:400;white-space:nowrap}
.main-nav{left:547px;top:28px;width:460px;font-size:13.5px;font-weight:400;letter-spacing:.2px;line-height:26px}
.main-nav ul{list-style:none;display:flex;gap:17px;white-space:nowrap}
.main-nav ul.secondary{font-size:11.5px;gap:14px;color:#4a5663}
.main-nav a{color:inherit;text-decoration:none}

.welcome-band{left:0;top:100px;width:1200px;height:102px;background:var(--band-light)}
.welcome-band .mid{position:absolute;left:0;top:34px;width:1200px;height:34px;background:var(--band-mid)}
.welcome-title{left:248px;top:133px;font-size:25px;font-weight:300;white-space:nowrap}
.quick-links{left:755px;top:100px;width:232px}
.quick-links a{display:block;height:33.5px;line-height:33.5px;text-align:center;color:#fff;text-decoration:none;font-size:13px;font-weight:500;white-space:nowrap}
.quick-links a:nth-child(1){background:var(--btn-1)}
.quick-links a:nth-child(2){background:var(--btn-2)}
.quick-links a:nth-child(3){background:var(--btn-3)}

.photo{background:linear-gradient(135deg,#6d5a46,#2a2624 55%,#8a8a86)}
.team-photo{left:253px;top:261px;width:390px;height:206px}
.intro-text{left:670px;top:263px;width:292px;font-size:10.3px;line-height:13px;font-weight:300}
.intro-text p{margin-bottom:13px}

.headline{left:312px;top:524px;font-size:58px;line-height:76px;font-weight:700;color:var(--accent);white-space:nowrap}

.hours{left:304px;top:774px;font-size:18.5px;line-height:22.2px;font-weight:300;white-space:nowrap}
.doctor-photo{left:665px;top:700px;width:296px;height:240px;background:linear-gradient(135deg,#a9c7bd,#e9e7e0 45%,#ef8a3c)}

.site-footer{left:0;top:986px;width:1200px;height:214px;background:var(--footer-bg)}
.footer-contact{left:238px;top:1005px;font-size:18.5px;line-height:22px;font-weight:300;white-space:nowrap}
.footer-address{left:238px;top:1134px;font-size:18.5px;line-height:22px;font-weight:300;white-space:nowrap}
.map{left:676px;top:996px;width:292px;height:189px;background:linear-gradient(160deg,#e9e5df,#dedad3)}
.curves{left:0;top:0;width:1200px;height:1200px;pointer-events:none}
</style>
</head>
<body>
<header class="site-header abs"></header>
<div class="brand-mark abs"></div>
<div class="brand-name abs">Dr. Maren Ostrova, DDS</div>
<div class="brand-tagline abs">Grins of Pellbrook</div>
<nav class="main-nav abs">
  <ul class="primary">
    <li><a href="#">ABOUT US</a></li><li><a href="#">CONTACT US</a></li><li><a href="#">SERVICES</a></li><li><a href="#">OUR STAFF</a></li><li><a href="#">TESTIMONIALS</a></li>
  </ul>
  <ul class="secondary">
    <li><a href="#">OUR OFFICES</a></li><li><a href="#">PATIENT EDUCATION</a></li><li><a href="#">PATIENT FORMS</a></li><li><a href="http://www.friendspace.example/Grins-of-Pellbrook-627150384019562">FRIENDSPACE</a></li>
  </ul>
</nav>

<section class="welcome-band abs"><div class="mid"></div></section>
<h1 class="welcome-title abs">A Warm Welcome to You &amp; Your Family</h1>
<div class="quick-links abs">
  <a href="#">Online Patient Form</a>
  <a href="#">info@grinsofpellbrook.example</a>
  <a href="#">555-014-2280/2281</a>
</div>

<div class="team-photo photo abs" role="img" aria-label="Group photo of the full dental team seated together"></div>
<div class="intro-text abs">
  <p>Dr. Maren Ostrova provides a full range of dental services to the whole family. Many of our patient families span multiple generations. Our Team are dedicated to taking the time needed to provide the very best care every patient deserves.</p>
  <p>Please tour our web site to learn more about family dentistry, cosmetic dentistry and our restorative dental services. We invite you to call us with any questions you may have - we all look forward to meeting you and your family!</p>
  <p>New patients looking for quality dental care in a relaxed environment are welcome! We accept PPO, Indeminity and Traditional Insurance plans.</p>
</div>

<h2 class="headline abs">Honestly Caring &amp;<br>Quality Dentistry</h2>

<div class="hours abs">
  Monday:&nbsp; 12:00pm to 6:00pm<br>
  Tuesday: 10:00am to 7:00pm<br>
  Wednesday: Closed<br>
  Thursday: 8:00am to 6:00pm<br>
  Friday: 8:00am to 5:00pm<br>
  Saturday when open: 8:00am to<br>
  3:00pm OR 8:00am to 12:00pm
</div>
<div class="doctor-photo photo abs" role="img" aria-label="Dentist in a white coat talking with a patient in the treatment chair"></div>

<svg class="curves abs" viewBox="0 0 1200 1200" aria-hidden="true">
  <g fill="none" stroke="var(--curve)" stroke-width="1.2">
    <path d="M247 240 Q444 294 641 240"/>
    <path d="M247 492 Q444 440 641 492"/>
    <path d="M664 235 Q812 190 962 235"/>
    <path d="M664 499 Q812 542 962 499"/>
    <path d="M247 708 Q444 762 641 708"/>
    <path d="M664 703 Q812 662 962 703"/>
  </g>
</svg>

<footer class="site-footer abs"></footer>
<div class="footer-contact abs">
  Call us at: 555-014-2280/2281<br>
  Email:<br>
  info@grinsofpellbrook.example<br>
  www.grinsofpellbrook.example
</div>
<div class="footer-address abs">
  418 E. Lindell Ave, Suite 2C<br>
  Pellbrook, IL 60999
</div>
<div class="map abs" role="img" aria-label="Street map showing the office location"></div>
</body>
</html>
```